【ワイヤーフレーム】
http://kovexa.hostmir.example/client-check/lumera/waiya.png
※極力ワイヤーフレームにそって作成して下さい。

【画像について】
各メニューに配置する写真とメインイメージの写真をお纏め致しました。
必ずこの写真を配置して下さい★
https://19.filevault.example/0827-3c7e1a9f40b2d65e8814a0c9f7d31b62

【今のサイトの問題点】
・何のメニューか分かりづらい
・鍼、カリオンの強みが弱い
・サイトからのお問い合わせが全くない

【TOPデザイン作成にあたっての要望】
・予約アイコンをつける
・ファイシャルメニューが一番売りたいメニューとなります。
デザインは目立つように作成して下さい。
・針、カリオン併用治療を押したい
・高級街にあるので高級感があるデザイン
・ピクセルノート、スナップロウのアイコンを配置する

【ターゲット】
・新規顧客さま
会社員、主婦、お金もっている30代~40代

【サイトの目的】
・集客
・店舗の強みの打ち出し

【サイトマップ】
①TOP
②ABOUT US スタッフ
③トータルビューティー
④フェイシャルビュティー
⑤インナービュティー
⑥コラーゲンマシーン
⑦遺伝子検査・腸内フローラ
⑧料金表
⑨メニュー内容
⑩ニュース一覧
⑪ニュース詳細
⑫ブログ一覧
⑬ブログ詳細
⑭鍼・カリオンの説明
⑮よくある質問
⑯アクセス、治療時間、お問い合わせ
⑰求人(非表示 ページには設けなくていいです)
⑱物販 (非表示 ページには設けなくていいです)
⑲実績
⑳お客様の声

【カラー】
・茶色
・グレー

【参考サイト】
https://www.velkanis.example/ https://moravel-co.example
https://www.lumera1954.example/
茶系、グレー系
【ワイヤーフレーム】
※極力ワイヤーフレームにそって作成して下さい。

【画像について】
必ずこの写真を配置して下さい★
暗めの印象で作成をお願い致します。
濃い色味7:明るい色味3
今回4日間だけ延長させて頂きます。

この度はたくさんの応募有難うございます。

またの機会に是非宜しくお願い致します!

```html
<!DOCTYPE html>
<html lang="ja">
<head>
<meta charset="utf-8">
<title>Lumera 鍼・カリオン サロン</title>
<link href="https://fonts.googleapis.com/css2?family=Cormorant+Garamond:wght@500;600&family=Noto+Serif+JP:wght@400;500;600&family=Noto+Sans+JP:wght@400;500&family=Great+Vibes&display=swap" rel="stylesheet">
<style>
:root{
  --ink:#3a2f27;
  --dark:#2b2019;
  --band:#3a2c22;
  --movie:#5f5750;
  --beige:#e8e0d6;
  --light:#f1efec;
  --gold:#b49a6a;
  --white:#ffffff;
  --muted:#8a7f76;
  --line:#d8d0c6;
}
*{margin:0;padding:0;box-sizing:border-box}
html,body{width:1200px;height:3864px;overflow:hidden}
body{background:var(--white);color:var(--ink);font-family:"Noto Sans JP",sans-serif;font-size:12px;position:relative}
.serif{font-family:"Noto Serif JP",serif}
.abs{position:absolute}
.ph{position:absolute}

/* hero */
.hero{position:absolute;left:0;top:0;width:1200px;height:536px}
.hero-photo{left:0;top:0;width:1200px;height:488px;background:linear-gradient(100deg,#6b4a2c 0%,#a77b4c 35%,#c9a276 60%,#8c6a47 85%,#5a4130 100%)}
.brand{position:absolute;left:0;width:1200px;top:60px;text-align:center;color:var(--white)}
.brand .crown{width:14px;height:14px;border-radius:50%;background:var(--white);margin:0 auto 6px}
.brand .name{font-family:"Cormorant Garamond",serif;font-size:48px;font-weight:600;line-height:1;letter-spacing:2px}
.brand .sub{font-family:"Cormorant Garamond",serif;font-size:12px;letter-spacing:3px;margin-top:4px}
.top-util{position:absolute;right:40px;top:22px;display:flex;gap:10px;align-items:center}
.top-util .sq{width:14px;height:14px;border:1px solid var(--white)}
.reserve{background:var(--dark);color:var(--white);font-size:11px;padding:8px 16px;letter-spacing:1px;margin-left:10px}
.tagline{position:absolute;left:0;width:1200px;top:196px;text-align:center;color:var(--white)}
.tagline h1{font-family:"Noto Serif JP",serif;font-weight:500;font-size:26px;letter-spacing:3px}
.tagline p{font-size:12px;line-height:2;margin-top:26px;letter-spacing:1px}
.gnav{position:absolute;left:0;top:488px;width:1200px;height:48px;background:var(--dark);display:flex;justify-content:center;align-items:center;gap:0}
.gnav a{color:var(--white);text-decoration:none;font-size:12px;letter-spacing:1px;padding:0 28px;border-left:1px solid #5a4a3d}
.gnav a:first-child{border-left:none}

/* headings */
.sec-title{text-align:center;font-family:"Cormorant Garamond",serif;font-size:22px;letter-spacing:4px;color:var(--ink)}
.sec-title::after{content:"";display:block;width:40px;height:1px;background:var(--gold);margin:10px auto 0}

/* menu */
.menu-title{position:absolute;top:590px;left:0;width:1200px}
.feature-photo{left:48px;top:660px;width:552px;height:230px;background:linear-gradient(90deg,#c99778,#e9c6ae 50%,#b98466)}
.feature-text{position:absolute;left:632px;top:670px;width:500px}
.feature-text .tag{font-size:11px;color:var(--gold);letter-spacing:1px}
.feature-text h2{font-family:"Noto Serif JP",serif;font-size:22px;font-weight:500;margin-top:8px;letter-spacing:1px}
.feature-text .lead{font-size:12px;margin-top:10px;color:var(--muted)}
.feature-text .body{font-size:12px;line-height:2;margin-top:22px}
.cards{position:absolute;left:48px;top:940px;display:flex;gap:16px}
.card{width:264px}
.card .img{height:208px}
.card h3{font-family:"Noto Serif JP",serif;font-size:14px;font-weight:500;margin-top:14px}
.card p{font-size:11px;color:var(--muted);margin-top:6px}
.c1{background:linear-gradient(135deg,#d9a88c,#f0cdb8)}
.c2{background:linear-gradient(135deg,#8e6a55,#d6b39c)}
.c3{background:linear-gradient(135deg,#b5392f,#e7b3a1)}
.c4{background:linear-gradient(135deg,#cfd6de,#f4f6f8)}

/* about band */
.about{position:absolute;left:0;top:1272px;width:1200px;height:240px;background:linear-gradient(90deg,#2e231b,#5a4636 50%,#2e231b);color:var(--white);text-align:center}
.about h2{font-family:"Noto Serif JP",serif;font-weight:500;font-size:20px;letter-spacing:3px;margin-top:54px}
.about p{font-size:12px;line-height:2.2;margin-top:22px;letter-spacing:.5px}

/* movie */
.movie{position:absolute;left:0;top:1512px;width:1200px;height:568px;background:var(--movie)}
.movie h2{font-family:"Great Vibes",cursive;font-weight:400;color:var(--white);font-size:32px;text-align:center;margin-top:42px}
.movie h2 span{display:inline-block;width:50px;height:1px;background:var(--white);vertical-align:middle;margin:0 14px}
.video{left:240px;top:108px;width:720px;height:404px;background:linear-gradient(90deg,#e9d2b6,#f4e6d4 40%,#c9b08f)}
.play{position:absolute;left:330px;top:172px;width:60px;height:40px;background:#1e1814;border-radius:4px}

/* voice */
.voice{position:absolute;left:0;top:2080px;width:1200px;height:640px;background:var(--beige)}
.voice .sec-title{margin-top:64px}
.vgrid{position:absolute;left:64px;top:136px;display:grid;grid-template-columns:516px 516px;gap:24px 40px}
.vcard{background:var(--white);height:212px;padding:30px;display:flex;gap:28px}
.vcard .img{width:150px;height:150px;background:var(--beige);flex:none}
.vcard h3{font-family:"Noto Serif JP",serif;font-size:14px;font-weight:500}
.vcard p{font-size:11px;line-height:2;margin-top:12px;color:var(--muted)}

/* social */
.social{position:absolute;left:0;top:2720px;width:1200px;height:260px}
.feed-widget{left:48px;top:36px;width:392px;height:196px;background:linear-gradient(180deg,#f3f1ee,#e6e0d8);border:1px solid var(--line)}
.snap-head{position:absolute;left:460px;top:36px;width:692px;display:flex;justify-content:space-between;align-items:center}
.snap-head .label{display:flex;gap:8px;align-items:center;font-family:"Cormorant Garamond",serif;font-size:18px}
.snap-head .label i{width:14px;height:14px;border:1.5px solid var(--ink);border-radius:50%}
.snap-head .more{font-size:10px;letter-spacing:2px;color:var(--muted)}
.snap-grid{position:absolute;left:460px;top:64px;display:grid;grid-template-columns:repeat(5,124px);gap:8px}
.snap-grid div{height:80px}

/* access */
.access{position:absolute;left:0;top:2980px;width:1200px;height:460px;background:var(--light)}
.acc-brand{position:absolute;left:120px;top:56px;color:var(--ink)}
.acc-brand .name{font-family:"Cormorant Garamond",serif;font-size:40px;font-weight:600;line-height:1}
.acc-brand .sub{font-family:"Cormorant Garamond",serif;font-size:11px;letter-spacing:3px}
.acc-info{position:absolute;left:120px;top:140px;font-size:12px;line-height:2}
.tel{display:flex;align-items:center;gap:8px;font-family:"Noto Serif JP",serif;font-size:28px;color:#8a6a3a;margin:10px 0}
.map{left:560px;top:80px;width:500px;height:280px;background:linear-gradient(135deg,#e4e4e2,#d2d2cf)}

/* footer */
.footer{position:absolute;left:0;top:3440px;width:1200px;height:300px;background:var(--dark);color:#d9cfc4}
.fcols{position:absolute;left:48px;top:40px;display:flex;gap:90px}
.fcols ul{list-style:none;font-size:11px;line-height:2.4}
.fsoc{position:absolute;right:48px;bottom:30px;display:flex;gap:10px}
.fsoc i{width:14px;height:14px;border:1px solid #d9cfc4}
.bottom{position:absolute;left:0;top:3740px;width:1200px;height:124px;background:var(--white)}
.bottom .copy{position:absolute;right:120px;top:30px;font-size:10px;color:var(--muted)}
.pagetop{position:absolute;right:48px;top:60px;text-align:center;font-size:9px;color:var(--muted)}
</style>
</head>
<body>

<header class="hero">
  <div class="ph hero-photo" role="img" aria-label="施術を受けてくつろぐ女性のメインイメージ写真"></div>
  <div class="top-util"><span class="sq"></span><span class="sq"></span><span class="reserve">Reservation</span></div>
  <div class="brand"><div class="crown"></div><div class="name">Lumera</div><div class="sub">Salon &amp; Beauty</div></div>
  <div class="tagline">
    <h1>願いいつまでもあなたにもっと輝いていてもらいたいという想いから</h1>
    <p>鍼とカリオンを組み合わせた独自の施術で、内側から輝く美しさをお届けします。<br>落ち着いた空間で、一人ひとりに合わせた丁寧なケアをご提供いたします。</p>
  </div>
  <nav class="gnav">
    <a>TOP</a><a>ABOUT US</a><a>鍼・カリオンとは</a><a>メニュー</a><a>料金表</a><a>ブログ</a><a>よくある質問</a><a>アクセス</a>
  </nav>
</header>

<section>
  <div class="menu-title"><h2 class="sec-title">MENU LIST</h2></div>
  <div class="ph feature-photo" role="img" aria-label="フェイシャル施術の写真"></div>
  <div class="feature-text">
    <div class="tag">― 一番人気の施術 ―</div>
    <h2>フェイシャルビューティーコース</h2>
    <div class="lead">鍼とカリオンの併用で肌本来の力を引き出します</div>
    <p class="body">お肌のハリとツヤを取り戻し、若々しい表情へと導きます。<br>くすみやたるみが気になる方に特におすすめのコースです。<br>一回の施術でも変化を実感していただけます。</p>
  </div>
  <div class="cards">
    <div class="card"><div class="img c1" role="img" aria-label="インナービューティー施術の写真"></div><h3>インナービューティーコース</h3><p>体の内側から美しさを整えます</p></div>
    <div class="card"><div class="img c2" role="img" aria-label="トータルビューティー施術の写真"></div><h3>トータルビューティー</h3><p>全身をまとめてケアするコース</p></div>
    <div class="card"><div class="img c3" role="img" aria-label="コラーゲンマシーンの写真"></div><h3>コラーゲンマシーン</h3><p>光でハリのある肌を目指します</p></div>
    <div class="card"><div class="img c4" role="img" aria-label="遺伝子検査キットの写真"></div><h3>遺伝子検査</h3><p>体質を知り最適なケアを選びます</p></div>
  </div>
</section>

<section class="about">
  <h2>鍼・カリオンとは?</h2>
  <p>鍼とカリオンを組み合わせることで、体の巡りを整え、自然治癒力を高めます。<br>お肌だけでなく、心と体のバランスを整え、内側から健やかな美しさへ導きます。<br>はじめての方にも安心して受けていただける、やさしい施術です。</p>
</section>

<section class="movie">
  <h2><span></span>Special Movie<span></span></h2>
  <div class="ph video" role="img" aria-label="サロン紹介動画のサムネイル">
    <svg class="play" viewBox="0 0 60 40"><rect width="60" height="40" rx="4" fill="#1e1814"/><polygon points="24,12 24,28 37,20" fill="#fff"/></svg>
  </div>
</section>

<section class="voice">
  <h2 class="sec-title">VOICE</h2>
  <div class="vgrid">
    <div class="vcard"><div class="img" role="img" aria-label="お客様の写真"></div><div><h3>M.M さん</h3><p>施術後すぐに肌の変化を感じました。スタッフの方も丁寧で、安心して通えるサロンです。</p></div></div>
    <div class="vcard"><div class="img" role="img" aria-label="お客様の写真"></div><div><h3>M.M さん</h3><p>落ち着いた空間でリラックスできました。続けて通うほどお肌の調子が良くなっています。</p></div></div>
    <div class="vcard"><div class="img" role="img" aria-label="お客様の写真"></div><div><h3>M.M さん</h3><p>鍼は初めてで不安でしたが、痛みもなく心地よかったです。友人にもすすめたいです。</p></div></div>
    <div class="vcard"><div class="img" role="img" aria-label="お客様の写真"></div><div><h3>M.M さん</h3><p>体の内側から元気になった気がします。毎月のご褒美として楽しみにしています。</p></div></div>
  </div>
</section>

<section class="social">
  <div class="ph feed-widget" role="img" aria-label="ピクセルノートのページ埋め込み"></div>
  <div class="snap-head"><div class="label"><i></i>Snaprow</div><div class="more">VIEW MORE</div></div>
  <div class="snap-grid" role="img" aria-label="スナップロウ投稿写真の一覧">
    <div style="background:#c9a27c"></div><div style="background:#e8d3bf"></div><div style="background:#b7453a"></div><div style="background:#d8b9a0"></div><div style="background:#a67e5e"></div>
    <div style="background:#e2c9b4"></div><div style="background:#9b6b4e"></div><div style="background:#d6a68a"></div><div style="background:#c14a3e"></div><div style="background:#e9dccf"></div>
  </div>
</section>

<section class="access">
  <div class="acc-brand"><div class="name">Lumera</div><div class="sub">Salon &amp; Beauty</div></div>
  <div class="acc-info">
    <div>〒107-0061 東京都港区北青山 3-12-8 ルメラビル 2F</div>
    <div>表参道駅 A3 出口より徒歩 4 分</div>
    <div class="tel">
      <svg width="22" height="22" viewBox="0 0 24 24"><path d="M6.6 10.8a15 15 0 0 0 6.6 6.6l2.2-2.2a1 1 0 0 1 1-.25 11.4 11.4 0 0 0 3.6.57 1 1 0 0 1 1 1V20a1 1 0 0 1-1 1A17 17 0 0 1 3 4a1 1 0 0 1 1-1h3.5a1 1 0 0 1 1 1 11.4 11.4 0 0 0 .57 3.6 1 1 0 0 1-.25 1z" fill="#8a6a3a"/></svg>
      03-5842-1937
    </div>
    <div>診療時間</div>
    <div>平日 10:00 〜 20:00</div>
    <div>土日祝 10:00 〜 18:00</div>
  </div>
  <div class="ph map" role="img" aria-label="サロン周辺の地図"></div>
</section>

<footer class="footer">
  <div class="fcols">
    <ul><li>TOP</li><li>ABOUT US スタッフ</li></ul>
    <ul><li>トータルビューティー</li><li>フェイシャルビューティー</li><li>インナービューティー</li><li>コラーゲンマシーン</li><li>遺伝子検査・腸内フローラ</li></ul>
    <ul><li>料金表</li><li>メニュー内容</li><li>ニュース</li><li>ブログ</li><li>鍼・カリオンの説明</li></ul>
    <ul><li>よくある質問</li><li>アクセス・お問い合わせ</li><li>実績</li><li>お客様の声</li></ul>
  </div>
  <div class="fsoc"><i></i><i></i></div>
</footer>

<div class="bottom">
  <div class="copy">Copyright © Lumera Salon &amp; Beauty All Rights Reserved.</div>
  <div class="pagetop">
    <svg width="20" height="12" viewBox="0 0 20 12"><polyline points="2,10 10,2 18,10" fill="none" stroke="#8a7f76" stroke-width="1.5"/></svg>
    <div>PAGE TOP</div>
  </div>
</div>

</body>
</html>
```